Wellness Thai Massage Geschäft benötigt eine Preis/Info Broschüre

Ein kleines Thai Massage Geschäft in Bayern: Kolavan Thaimassage
Benötigt eine kleine Preisliste, sowie eine kurze Beschreibung vom Unternehmen. Angeboten werden traditionelle Thaimassagen. Der Farbstil soll dem Logo (Anhang) angepasst sein. Alle Bilder außer die Bilder von der Geschäftsführerin sind optional zur Verwendung verfügbar. Mehr Info wie Preise, etc. sind verfügbar auf der Website https://www.kolavanthaimassage.example/

```html
<!DOCTYPE html>
<html lang="de">
<head>
<meta charset="utf-8">
<title>Kolavan Thaimassage – Broschüre</title>
<link rel="stylesheet" href="https://fonts.googleapis.com/css2?family=Quicksand:wght@400;500;600;700&display=swap">
<style>
:root{
  --red:#a3161e;
  --red-dark:#861319;
  --red-bright:#e2383c;
  --text-red:#c9222b;
  --cream:#fdf6dc;
  --gold:#fbe894;
  --gold-soft:#f6e7a8;
  --white:#ffffff;
}
*{margin:0;padding:0;box-sizing:border-box}
html,body{width:766px;height:1200px;overflow:hidden;background:var(--white)}
body{font-family:"Quicksand",sans-serif;position:relative}
.sheet{position:absolute;left:28px;width:712px;height:553px;overflow:hidden;box-shadow:0 1px 4px rgba(0,0,0,.25)}
.sheet--outside{top:34px;background:var(--cream)}
.sheet--inside{top:616px}
.abs{position:absolute}
.waves{position:absolute;left:0;top:0;width:712px;height:553px}

/* outside */
.panel-mid{left:241px;top:0;width:231px;height:400px;background:linear-gradient(90deg,var(--red-dark),var(--red) 60%,#b81c24)}
.photo-products{left:0;top:146px;width:241px;height:240px;background:linear-gradient(160deg,#e9e2e4 0%,#b9a7a5 35%,#6d5d5f 55%,#c8a58e 80%,#b88a8c 100%)}
.photo-therapist{left:472px;top:0;width:240px;height:320px;background:linear-gradient(150deg,#e9e4e2 0%,#b42a2f 35%,#8f1f25 60%,#e7c5a6 85%,#d8d4dc 100%)}

.service-icon{width:30px;height:30px;border-radius:50%;background:var(--text-red);border:2px solid var(--cream);box-shadow:0 0 0 1.2px var(--text-red)}
.service-icon::after{content:"";position:absolute;left:7px;top:7px;width:12px;height:12px;border-radius:50%;border:1.3px solid var(--cream)}
.service-title{color:var(--text-red);font-size:12.5px;font-weight:500;line-height:12.5px}
.service-text{font-size:7.4px;line-height:9.7px;color:#4a1a18;letter-spacing:.15px}
.price{background:linear-gradient(90deg,var(--red-dark),var(--text-red));color:var(--gold);font-size:7.8px;line-height:8.4px;font-weight:500;border-radius:0 11px 11px 11px;padding:3px 9px;letter-spacing:.3px}
.price b{font-weight:700}

.brand-small{left:241px;width:231px;top:34px;text-align:center}
.brand-name{color:var(--gold);font-weight:600;text-transform:uppercase;letter-spacing:2px}
.brand-small .brand-name{font-size:15px;line-height:23px;display:inline-block;text-align:left;padding-left:24px;position:relative}
.brand-dot{position:absolute;left:0;top:9px;width:14px;height:14px;border-radius:50%;border:1.2px solid var(--gold)}
.rule{height:1px;background:var(--gold)}

.info-box{left:268px;top:122px;width:177px;height:176px;border:1.5px solid var(--gold);color:var(--gold);text-align:center}
.info-box h2{font-size:12.5px;font-weight:500;margin-top:13px;letter-spacing:.3px}
.info-box .hours{font-size:7.5px;line-height:11.5px;margin-top:5px}
.info-box h3{font-size:11.5px;font-weight:500;margin-top:8px}
.info-box .underline{width:60px;height:1px;background:var(--gold);margin:3px auto 5px}
.info-box .note{font-size:8.8px;line-height:11.5px;padding:0 6px}

.contact{left:241px;width:231px;text-align:center;color:var(--cream);font-size:6.8px;letter-spacing:.2px}
.contact-icon{width:16px;height:16px;border-radius:50%;background:var(--gold);margin:0 auto 3px;display:flex;align-items:center;justify-content:center}
.contact-icon svg{width:9px;height:9px}

.brand-large{left:518px;top:402px;width:194px}
.brand-large .brand-name{font-size:19px;line-height:25px;letter-spacing:2.5px;padding-left:32px;position:relative}
.brand-large .brand-dot{left:0;top:12px;width:24px;height:24px}
.tagline{color:var(--cream);font-size:8.8px;font-weight:600;letter-spacing:.6px;text-align:center;margin-top:10px;width:160px;margin-left:16px}
.tagline .rule{width:52px;margin:3px auto 0;background:var(--cream)}

/* inside */
.photo-session{left:0;top:0;width:440px;height:200px}
.floral-band{left:0;top:0;width:712px;height:553px}
.about{left:498px;width:200px;color:var(--gold)}
.about h2{font-size:12.5px;font-weight:500;line-height:12.5px}
.tick-item{display:flex;gap:5px;margin-top:9px}
.tick-item svg{flex:0 0 8px;width:8px;height:8px;margin-top:1px}
.tick-item p{font-size:7.3px;line-height:9.7px;color:var(--cream);letter-spacing:.15px}
</style>
</head>
<body>

<!-- Outside spread -->
<section class="sheet sheet--outside">
  <div class="abs panel-mid"></div>
  <div class="abs photo-products" role="img" aria-label="Foto: Massageöle, Fußcremes und gestapelte Hot Stones"></div>
  <div class="abs photo-therapist" role="img" aria-label="Foto: Therapeutin bei einer Dehnung während einer Thai-Massage"></div>

  <svg class="waves" viewBox="0 0 712 553" aria-hidden="true">
    <defs>
      <linearGradient id="sweep" x1="0" y1="0" x2="1" y2="0">
        <stop offset="0" stop-color="#e2383c"/>
        <stop offset=".35" stop-color="#8c141b"/>
        <stop offset=".7" stop-color="#a8161e"/>
        <stop offset="1" stop-color="#8e141a"/>
      </linearGradient>
      <linearGradient id="creamband" x1="0" y1="0" x2="1" y2="0">
        <stop offset="0" stop-color="#fdf3c8"/>
        <stop offset="1" stop-color="#fbef9a"/>
      </linearGradient>
    </defs>
    <path d="M0,364 C160,392 320,366 460,306 C560,266 650,272 712,264 L712,553 L0,553 Z" fill="url(#creamband)"/>
    <path d="M0,378 C160,406 320,382 460,322 C560,284 650,294 712,296 L712,553 L0,553 Z" fill="url(#sweep)"/>
    <path d="M0,546 C250,560 520,530 712,490 L712,553 L0,553 Z" fill="url(#creamband)"/>
  </svg>

  <!-- Back panel -->
  <div class="abs service-icon" style="left:34px;top:21px"></div>
  <h2 class="abs service-title" style="left:69px;top:30px">Rücken-Thai Massage</h2>
  <p class="abs service-text" style="left:34px;top:56px;width:180px">Bei dieser Massagetechnik wird größtenteils der Rücken sowie auch Nacken, Hinterkopf, Schulter und Finger involviert. Diese Massage eignet sich besonders falls eines dieser Bereiche verspannt oder Schmerzen verursacht.</p>
  <div class="abs price" style="left:34px;top:122px;width:104px"><b>30</b> Minuten - <b>35</b> Euro<br><b>60</b> Minuten - <b>72</b> Euro</div>

  <!-- Middle panel -->
  <div class="abs brand-small">
    <div class="brand-name"><span class="brand-dot"></span>Kolavan<br>Thaimassage</div>
    <div class="rule" style="width:148px;margin:5px auto 0"></div>
  </div>

  <div class="abs info-box">
    <h2>Öffnungszeiten:</h2>
    <p class="hours">Montag: 9.00 - 20.00 Uhr<br>Dienstag - Freitag: 10.00 - 20.00 Uhr<br>Samstag: 10.00 - 18.00 Uhr<br>Sonntag: Ruhetag</p>
    <h3>Terminvereinbarung:</h3>
    <div class="underline"></div>
    <p class="note">Damit wir uns die Zeit nehmen können, bitten wir sie ihren Termin im Vorfeld telefonisch mit uns zu vereinbaren</p>
  </div>

  <div class="abs contact" style="top:385px">
    <div class="contact-icon"><svg viewBox="0 0 10 10"><path d="M2.2 1 L3.6 1 L4.2 3 L3.2 3.8 C3.7 5 4.8 6.1 6 6.6 L6.8 5.6 L8.8 6.2 L8.8 7.6 C8.8 8.4 8 9 7.2 8.9 C4 8.4 1.4 5.8 1 2.6 C0.9 1.8 1.4 1 2.2 1 Z" fill="#c9222b"/></svg></div>
    01701234567
  </div>
  <div class="abs contact" style="top:418px">
    <div class="contact-icon"><svg viewBox="0 0 10 10"><circle cx="5" cy="5" r="4" fill="none" stroke="#c9222b" stroke-width="1.2"/><path d="M1 5 H9 M5 1 C3 3 3 7 5 9 C7 7 7 3 5 1" fill="none" stroke="#c9222b" stroke-width=".9"/></svg></div>
    www.kolavanthaimassage.example
  </div>
  <div class="abs contact" style="top:453px">
    <div class="contact-icon"><svg viewBox="0 0 10 10"><rect x="1" y="2.2" width="8" height="5.8" rx=".8" fill="#c9222b"/><path d="M1.3 2.6 L5 5.4 L8.7 2.6" fill="none" stroke="#fbe894" stroke-width=".8"/></svg></div>
    kolavan.thaimassage@example.com
  </div>
  <div class="abs contact" style="top:488px;line-height:10.5px">
    <div class="contact-icon"><svg viewBox="0 0 10 10"><path d="M5 9.5 C3 7 1.8 5.4 1.8 3.8 A3.2 3.2 0 0 1 8.2 3.8 C8.2 5.4 7 7 5 9.5 Z" fill="#c9222b"/><circle cx="5" cy="3.8" r="1.2" fill="#fbe894"/></svg></div>
    Lindenweg 14b<br>Musterhausen 83600
  </div>

  <!-- Front panel -->
  <div class="abs brand-large">
    <div class="brand-name"><span class="brand-dot"></span>Kolavan<br>Thaimassage</div>
    <div class="tagline">Wellness Thai Massage<div class="rule"></div></div>
  </div>
</section>

<!-- Inside spread -->
<section class="sheet sheet--inside">
  <svg class="waves" viewBox="0 0 712 553" aria-hidden="true">
    <defs>
      <linearGradient id="redbg" x1="0" y1="0" x2="1" y2="1">
        <stop offset="0" stop-color="#8e141a"/>
        <stop offset=".6" stop-color="#a8161e"/>
        <stop offset="1" stop-color="#e2383c"/>
      </linearGradient>
      <linearGradient id="session" x1="0" y1="0" x2="1" y2="1">
        <stop offset="0" stop-color="#8f1f22"/>
        <stop offset=".3" stop-color="#c04a2c"/>
        <stop offset=".55" stop-color="#e9c36a"/>
        <stop offset=".8" stop-color="#cfd3dc"/>
        <stop offset="1" stop-color="#b02a2e"/>
      </linearGradient>
      <linearGradient id="floral" x1="0" y1="0" x2="0" y2="1">
        <stop offset="0" stop-color="#fbe2b8"/>
        <stop offset="1" stop-color="#f8c7b0"/>
      </linearGradient>
    </defs>
    <rect width="712" height="553" fill="url(#redbg)"/>
    <path d="M472,44 C560,18 650,40 712,118" fill="none" stroke="#fbe894" stroke-width="7"/>
    <path d="M0,150 C130,212 300,204 472,52 L472,553 L0,553 Z" fill="#e2383c"/>
    <path d="M0,160 C130,222 300,214 472,60 L472,553 L0,553 Z" fill="#fdf6dc"/>
    <path d="M0,0 L440,0 C410,70 360,125 290,165 C200,205 80,190 0,146 Z" fill="url(#session)"/>
    <path d="M0,404 C100,470 210,500 310,497 C420,492 520,440 712,424 L712,553 L0,553 Z" fill="#e2383c"/>
    <path d="M0,412 C100,478 210,506 310,503 C420,498 520,446 712,430 L712,553 L0,553 Z" fill="url(#floral)"/>
  </svg>
  <div class="abs photo-session" role="img" aria-label="Foto: Therapeutin massiert Nacken und Schultern einer Kundin"></div>
  <div class="abs floral-band" style="top:430px;height:123px" role="img" aria-label="Dekoratives Orchideen-Linienmuster in Rot auf Creme"></div>

  <!-- Left column -->
  <div class="abs service-icon" style="left:34px;top:205px"></div>
  <h2 class="abs service-title" style="left:69px;top:214px">Hot Stone Massage</h2>
  <p class="abs service-text" style="left:34px;top:239px;width:178px">Bei der Hot Stone Massage werden angewärmte Vulkansteine entlag der Energielinien angebracht. Durch die abgegebene gespeicherte Wärme wird der Energiefluss und die Blutzirkulation gesteigert. Es kommt im ganzen Körper zu einer Tiefenentspannung</p>
  <div class="abs price" style="left:34px;top:315px;width:105px;padding-top:7px;padding-bottom:7px"><b>90</b> Minuten - <b>83</b> Euro</div>

  <div class="abs service-icon" style="left:34px;top:343px"></div>
  <h2 class="abs service-title" style="left:69px;top:352px">Fussreflexzonen Massage</h2>
  <p class="abs service-text" style="left:34px;top:380px;width:180px">Eine Massage für den wohl für den strapaziertesten Körperteil, den Füssen, setzt neue Kräfte frei und verleiht Vitalität</p>
  <div class="abs price" style="left:34px;top:417px;width:104px"><b>30</b> Minuten - <b>35</b> Euro<br><b>60</b> Minuten - <b>62</b> Euro</div>

  <!-- Middle column -->
  <div class="abs service-icon" style="left:253px;top:182px"></div>
  <h2 class="abs service-title" style="left:290px;top:184px">Traditionelle Thai-Sport<br>Massage</h2>
  <p class="abs service-text" style="left:252px;top:216px;width:180px">Mt der traditionellen Thai-Massage werden durch Akupressur, Dehnung und Energielinien-Massage Energieblockaden gelöst. Es wird an 10 Energiepunkten und Linien massiert, die für den Einklang von Körper und Geist wichtig sind. Somit wird eine innere Balance und der Fluss der Lebensenergie erreicht</p>
  <div class="abs price" style="left:253px;top:298px;width:103px"><b>60</b> Minuten - <b>54</b> Euro<br><b>90</b> Minuten - <b>76</b> Euro</div>

  <div class="abs service-icon" style="left:253px;top:325px"></div>
  <h2 class="abs service-title" style="left:290px;top:334px">Aromaöl Massage</h2>
  <p class="abs service-text" style="left:252px;top:361px;width:176px">Die Aromaöl Massage ist eine Behandlungsform zur Regeneration und Harmonisierung des gesamten Körpers. Dabei wird das Basisöl mit ätherischen Ölen angereichert. Die Aromatherapie kann anregend oder entspannend abgestimmt werden</p>
  <div class="abs price" style="left:253px;top:431px;width:103px"><b>60</b> Minuten - <b>51</b> Euro<br><b>90</b> Minuten - <b>72</b> Euro</div>

  <!-- Right panel -->
  <div class="abs about" style="top:82px">
    <h2>Was ist Thai Massage<br>eigentlich?</h2>
    <div class="tick-item">
      <svg viewBox="0 0 10 10"><path d="M1 5.5 L4 8.5 L9 1.5" fill="none" stroke="#fbe894" stroke-width="2"/></svg>
      <p>Thai Massage existiert schon seit ca. über 2500 Jahren welches sich im Laufe der Zeit zu einer effektiven Methode gegen Schmerzzustände und auch Krankheiten entwickelt welches in der heutigen Zeit sogar Kultstatus erreicht hat. Diese thailändische Heilungsmethode verlangt eine professionelle Ausbildung die Hintergrundwissen und langes Training mit sich bringt.</p>
    </div>
    <h2 style="margin-top:19px">Über uns</h2>
    <div class="tick-item" style="margin-top:12px">
      <svg viewBox="0 0 10 10"><path d="M1 5.5 L4 8.5 L9 1.5" fill="none" stroke="#fbe894" stroke-width="2"/></svg>
      <p>Kolavan Thaimassage legt einen hohen Wert auf die Zufriedenheit und das Wohlbefinden von jedem Kunden. Wenn sie also z.B nach viel Arbeit gestresst sind und Schmerzen an einer bestimmten Region aufgebaut haben, dann sind sie bei uns an der richtigen Adresse. Geführt wird das Massagestudio von Suda Berger, die professionell ausgebildet wurde und auch beruflich schon in Deutschland sowie in Thailand viel Erfahrung gesammelt hat. Wir freuen uns schon auf ihren Besuch bei Kolavan</p>
    </div>
  </div>
</section>

</body>
</html>
```